Flavour Wheel - Illustrator Graph

I need my basic layout, from the sample I provided, turned into a professional looking flavour wheel.

I have attached a sample of a final design I like, but please use your own creativity also.

All the exact words I need are on the uploaded illustration.

I would need the file supplied to me in .ai

Industry/Entity Type

Wheel

Font styles to use
Sans Serif

Colors

Designer to choose colors to be used in the design.

Requirements
Must have
• Files must be supplied in .ai format with fonts not outlined.
• I need each segment separated so I can change the colours if needed myself.
Nice to have
• I like small white gaps between the sections.

```html
<!DOCTYPE html>
<html lang="en">
<head>
<meta charset="utf-8">
<title>Flavour Wheel</title>
<link rel="stylesheet" href="https://fonts.googleapis.com/css2?family=Jost:wght@400;500;600;700&display=swap">
<style>
:root{
  --bg:#ffffff;
  --gap:#ffffff;
  --sour:#dc1f2a;--earthy:#ebb321;--sweet:#1b7a3e;--salty:#1aa0b5;
  --savoury:#d24a34;--spicy:#b01f3f;--smokey:#a57a62;
  --vinegary:#a7b0b3;--citrus:#3aa35a;--floral:#e04450;--herby:#37a155;
  --nutty:#e0ad62;--buttery:#cf9c2b;--fruity-sweet:#a3b53a;--sugary:#9eaaa9;
  --caramel:#2e9e56;--charred:#5a9a7c;--briny:#9daaaa;--meatiness:#6fc1cc;
  --umami:#c8a46b;--chilli:#ef6b52;--peppery:#c8303e;--cajun:#7f3f98;
  --woody:#c0834c;--fruity-smoke:#2aa86a;--acid:#e96b9b;--bitter:#9e5b74;
  --label:#ffffff;
}
html,body{margin:0;padding:0;width:1200px;height:927px;overflow:hidden;background:var(--bg);}
.flavour-wheel{display:block;width:1200px;height:927px;font-family:"Jost",sans-serif;}
.band{fill:none;}
.core .band{stroke-width:135;}
.family .band{stroke-width:80;}
.divider{stroke:var(--gap);stroke-width:2.5;}
.ring-gap{fill:none;stroke:var(--gap);stroke-width:2.5;}
.hub{fill:var(--bg);}
.core-label{fill:var(--label);font-size:22px;font-weight:700;dominant-baseline:central;text-anchor:middle;}
.family-label{fill:var(--label);font-size:14px;font-weight:500;dominant-baseline:central;text-anchor:middle;}
.note rect{fill:var(--c);}
.note text{fill:var(--c);font-size:15px;font-weight:500;dominant-baseline:central;}
.note.out text{text-anchor:start;}
.note.in text{text-anchor:end;}
</style>
</head>
<body>
<svg class="flavour-wheel" viewBox="0 0 1200 927" xmlns="http://www.w3.org/2000/svg" role="img" aria-label="Flavour wheel">
<g transform="translate(606 462)">

  <g class="core">
    <circle class="band" r="102.5" pathLength="360" stroke="var(--sour)" stroke-dasharray="72 288" transform="rotate(228)"/>
    <circle class="band" r="102.5" pathLength="360" stroke="var(--earthy)" stroke-dasharray="73 287" transform="rotate(-60)"/>
    <circle class="band" r="102.5" pathLength="360" stroke="var(--sweet)" stroke-dasharray="62 298" transform="rotate(13)"/>
    <circle class="band" r="102.5" pathLength="360" stroke="var(--salty)" stroke-dasharray="32 328" transform="rotate(75)"/>
    <circle class="band" r="102.5" pathLength="360" stroke="var(--savoury)" stroke-dasharray="35 325" transform="rotate(107)"/>
    <circle class="band" r="102.5" pathLength="360" stroke="var(--spicy)" stroke-dasharray="48 312" transform="rotate(142)"/>
    <circle class="band" r="102.5" pathLength="360" stroke="var(--smokey)" stroke-dasharray="38 322" transform="rotate(190)"/>
  </g>

  <g class="family">
    <circle class="band" r="210" pathLength="360" stroke="var(--vinegary)" stroke-dasharray="20 340" transform="rotate(252)"/>
    <circle class="band" r="210" pathLength="360" stroke="var(--citrus)" stroke-dasharray="16 344" transform="rotate(-88)"/>
    <circle class="band" r="210" pathLength="360" stroke="var(--floral)" stroke-dasharray="12 348" transform="rotate(-72)"/>
    <circle class="band" r="210" pathLength="360" stroke="var(--herby)" stroke-dasharray="45 315" transform="rotate(-60)"/>
    <circle class="band" r="210" pathLength="360" stroke="var(--nutty)" stroke-dasharray="28 332" transform="rotate(-15)"/>
    <circle class="band" r="210" pathLength="360" stroke="var(--buttery)" stroke-dasharray="13 347" transform="rotate(13)"/>
    <circle class="band" r="210" pathLength="360" stroke="var(--fruity-sweet)" stroke-dasharray="14 346" transform="rotate(26)"/>
    <circle class="band" r="210" pathLength="360" stroke="var(--sugary)" stroke-dasharray="18 342" transform="rotate(40)"/>
    <circle class="band" r="210" pathLength="360" stroke="var(--caramel)" stroke-dasharray="17 343" transform="rotate(58)"/>
    <circle class="band" r="210" pathLength="360" stroke="var(--charred)" stroke-dasharray="16 344" transform="rotate(75)"/>
    <circle class="band" r="210" pathLength="360" stroke="var(--briny)" stroke-dasharray="16 344" transform="rotate(91)"/>
    <circle class="band" r="210" pathLength="360" stroke="var(--meatiness)" stroke-dasharray="17 343" transform="rotate(107)"/>
    <circle class="band" r="210" pathLength="360" stroke="var(--umami)" stroke-dasharray="18 342" transform="rotate(124)"/>
    <circle class="band" r="210" pathLength="360" stroke="var(--chilli)" stroke-dasharray="30 330" transform="rotate(142)"/>
    <circle class="band" r="210" pathLength="360" stroke="var(--peppery)" stroke-dasharray="18 342" transform="rotate(172)"/>
    <circle class="band" r="210" pathLength="360" stroke="var(--cajun)" stroke-dasharray="7 353" transform="rotate(190)"/>
    <circle class="band" r="210" pathLength="360" stroke="var(--woody)" stroke-dasharray="13 347" transform="rotate(197)"/>
    <circle class="band" r="210" pathLength="360" stroke="var(--fruity-smoke)" stroke-dasharray="18 342" transform="rotate(210)"/>
    <circle class="band" r="210" pathLength="360" stroke="var(--acid)" stroke-dasharray="12 348" transform="rotate(228)"/>
    <circle class="band" r="210" pathLength="360" stroke="var(--bitter)" stroke-dasharray="12 348" transform="rotate(240)"/>
  </g>

  <g class="gaps">
    <circle class="ring-gap" r="170"/>
    <line class="divider" y1="-35" y2="-251" transform="rotate(318)"/>
    <line class="divider" y1="-35" y2="-251" transform="rotate(30)"/>
    <line class="divider" y1="-35" y2="-251" transform="rotate(103)"/>
    <line class="divider" y1="-35" y2="-251" transform="rotate(165)"/>
    <line class="divider" y1="-35" y2="-251" transform="rotate(197)"/>
    <line class="divider" y1="-35" y2="-251" transform="rotate(232)"/>
    <line class="divider" y1="-35" y2="-251" transform="rotate(280)"/>
    <line class="divider" y1="-170" y2="-251" transform="rotate(342)"/>
    <line class="divider" y1="-170" y2="-251" transform="rotate(2)"/>
    <line class="divider" y1="-170" y2="-251" transform="rotate(18)"/>
    <line class="divider" y1="-170" y2="-251" transform="rotate(75)"/>
    <line class="divider" y1="-170" y2="-251" transform="rotate(116)"/>
    <line class="divider" y1="-170" y2="-251" transform="rotate(130)"/>
    <line class="divider" y1="-170" y2="-251" transform="rotate(148)"/>
    <line class="divider" y1="-170" y2="-251" transform="rotate(181)"/>
    <line class="divider" y1="-170" y2="-251" transform="rotate(214)"/>
    <line class="divider" y1="-170" y2="-251" transform="rotate(262)"/>
    <line class="divider" y1="-170" y2="-251" transform="rotate(287)"/>
    <line class="divider" y1="-170" y2="-251" transform="rotate(300)"/>
    <line class="divider" y1="-170" y2="-251" transform="rotate(330)"/>
    <circle class="hub" r="35"/>
  </g>

  <g class="core-labels">
    <text class="core-label" x="0" y="-110">Sour</text>
    <text class="core-label" x="108" transform="rotate(-24)">Earthy</text>
    <text class="core-label" x="108" transform="rotate(44)">Sweet</text>
    <text class="core-label" x="-108" transform="rotate(271)">Salty</text>
    <text class="core-label" x="-108" transform="rotate(304.5)">Savoury</text>
    <text class="core-label" x="-108" transform="rotate(346)">Spicy</text>
    <text class="core-label" x="-108" transform="rotate(29)">Smokey</text>
  </g>

  <g class="family-labels">
    <text class="family-label" x="-210" transform="rotate(82)">Vinegary</text>
    <text class="family-label" x="210" transform="rotate(-80)">Citrus</text>
    <text class="family-label" x="210" transform="rotate(-66)">Floral</text>
    <text class="family-label" x="210" transform="rotate(-37.5)">Herby</text>
    <text class="family-label" x="210" transform="rotate(-1)">Nutty</text>
    <text class="family-label" x="210" transform="rotate(19.5)">Buttery</text>
    <text class="family-label" x="210" transform="rotate(33)">Fruity</text>
    <text class="family-label" x="210" transform="rotate(49)">Sugary</text>
    <text class="family-label" x="210" transform="rotate(66.5)">Caramel</text>
    <text class="family-label" x="210" transform="rotate(83)">Charred</text>
    <text class="family-label" x="-210" transform="rotate(279)">Briny</text>
    <text class="family-label" x="-210" transform="rotate(295.5)">Meatiness</text>
    <text class="family-label" x="-210" transform="rotate(313)">Umami</text>
    <text class="family-label" x="-210" transform="rotate(337)">Chilli</text>
    <text class="family-label" x="-210" transform="rotate(1)">Peppery</text>
    <text class="family-label" x="-210" transform="rotate(13.5)">Cajun</text>
    <text class="family-label" x="-210" transform="rotate(23.5)">Woody</text>
    <text class="family-label" x="-210" transform="rotate(39)">Fruity</text>
    <text class="family-label" x="-210" transform="rotate(54)">Acid</text>
    <text class="family-label" x="-210" transform="rotate(66)">Bitter</text>
  </g>

  <g class="notes">
    <g class="note out" style="--c:#7bbf5b" transform="rotate(6)"><rect x="-7" y="-270" width="14" height="14"/><text x="278" transform="rotate(-90)">Sumac</text></g>
    <g class="note out" style="--c:#b9d3b0" transform="rotate(10)"><rect x="-7" y="-270" width="14" height="14"/><text x="278" transform="rotate(-90)">Zest</text></g>
    <g class="note out" style="--c:#1e6b3a" transform="rotate(14)"><rect x="-7" y="-270" width="14" height="14"/><text x="278" transform="rotate(-90)">Lime</text></g>
    <g class="note out" style="--c:#d2db45" transform="rotate(18)"><rect x="-7" y="-270" width="14" height="14"/><text x="278" transform="rotate(-90)">Lemon</text></g>
    <g class="note out" style="--c:#e8375a" transform="rotate(27)"><rect x="-7" y="-270" width="14" height="14"/><text x="278" transform="rotate(-90)">Coriander</text></g>
    <g class="note out" style="--c:#3aa04a" transform="rotate(31)"><rect x="-7" y="-270" width="14" height="14"/><text x="278" transform="rotate(-90)">Celery</text></g>
    <g class="note out" style="--c:#7cc47a" transform="rotate(41)"><rect x="-7" y="-270" width="14" height="14"/><text x="278" transform="rotate(-90)">Tea</text></g>
    <g class="note out" style="--c:#b9d6b2" transform="rotate(45)"><rect x="-7" y="-270" width="14" height="14"/><text x="278" transform="rotate(-90)">Sage</text></g>
    <g class="note out" style="--c:#a3cb97" transform="rotate(49)"><rect x="-7" y="-270" width="14" height="14"/><text x="278" transform="rotate(-90)">Thyme</text></g>
    <g class="note out" style="--c:#82b98a" transform="rotate(53)"><rect x="-7" y="-270" width="14" height="14"/><text x="278" transform="rotate(-90)">Rosemary</text></g>
    <g class="note out" style="--c:#4aa24e" transform="rotate(57)"><rect x="-7" y="-270" width="14" height="14"/><text x="278" transform="rotate(-90)">Bay Leaf</text></g>
    <g class="note out" style="--c:#b0d4a8" transform="rotate(61)"><rect x="-7" y="-270" width="14" height="14"/><text x="278" transform="rotate(-90)">Fennel</text></g>
    <g class="note out" style="--c:#1a5e2a" transform="rotate(65)"><rect x="-7" y="-270" width="14" height="14"/><text x="278" transform="rotate(-90)">Five Spice</text></g>
    <g class="note out" style="--c:#6b5548" transform="rotate(78)"><rect x="-7" y="-270" width="14" height="14"/><text x="278" transform="rotate(-90)">Nutmeg</text></g>
    <g class="note out" style="--c:#f08a24" transform="rotate(82)"><rect x="-7" y="-270" width="14" height="14"/><text x="278" transform="rotate(-90)">Turmeric</text></g>
    <g class="note out" style="--c:#f2a86b" transform="rotate(86)"><rect x="-7" y="-270" width="14" height="14"/><text x="278" transform="rotate(-90)">Star Anise</text></g>
    <g class="note out" style="--c:#f4c49a" transform="rotate(90)"><rect x="-7" y="-270" width="14" height="14"/><text x="278" transform="rotate(-90)">Cinnamon</text></g>
    <g class="note out" style="--c:#a35a10" transform="rotate(94)"><rect x="-7" y="-270" width="14" height="14"/><text x="278" transform="rotate(-90)">Clove</text></g>
    <g class="note out" style="--c:#d9ad8c" transform="rotate(98)"><rect x="-7" y="-270" width="14" height="14"/><text x="278" transform="rotate(-90)">Pecan</text></g>
    <g class="note out" style="--c:#e05a2a" transform="rotate(102)"><rect x="-7" y="-270" width="14" height="14"/><text x="278" transform="rotate(-90)">Coffee</text></g>
    <g class="note out" style="--c:#cf9a6a" transform="rotate(106)"><rect x="-7" y="-270" width="14" height="14"/><text x="278" transform="rotate(-90)">Butter</text></g>
    <g class="note out" style="--c:#178a58" transform="rotate(116)"><rect x="-7" y="-270" width="14" height="14"/><text x="278" transform="rotate(-90)">Fruit Juice</text></g>
    <g class="note out" style="--c:#a9d6bc" transform="rotate(120)"><rect x="-7" y="-270" width="14" height="14"/><text x="278" transform="rotate(-90)">Fruits</text></g>
    <g class="note out" style="--c:#c4222f" transform="rotate(124)"><rect x="-7" y="-270" width="14" height="14"/><text x="278" transform="rotate(-90)">Sauce/Ketchup</text></g>
    <g class="note out" style="--c:#7a2a10" transform="rotate(133)"><rect x="-7" y="-270" width="14" height="14"/><text x="278" transform="rotate(-90)">Cola</text></g>
    <g class="note out" style="--c:#c9d36a" transform="rotate(137)"><rect x="-7" y="-270" width="14" height="14"/><text x="278" transform="rotate(-90)">Agave Nectar</text></g>
    <g class="note out" style="--c:#dfe48a" transform="rotate(141)"><rect x="-7" y="-270" width="14" height="14"/><text x="278" transform="rotate(-90)">Sugars</text></g>
    <g class="note out" style="--c:#e6dc6a" transform="rotate(145)"><rect x="-7" y="-270" width="14" height="14"/><text x="278" transform="rotate(-90)">Honey</text></g>
    <g class="note out" style="--c:#7ac043" transform="rotate(149)"><rect x="-7" y="-270" width="14" height="14"/><text x="278" transform="rotate(-90)">Molasses</text></g>
    <g class="note out" style="--c:#f2d800" transform="rotate(153)"><rect x="-7" y="-270" width="14" height="14"/><text x="278" transform="rotate(-90)">Maple Syrup</text></g>
    <g class="note out" style="--c:#3a3f42" transform="rotate(162.5)"><rect x="-7" y="-270" width="14" height="14"/><text x="278" transform="rotate(-90)">Anchovies</text></g>
    <g class="note out" style="--c:#4a5055" transform="rotate(166.5)"><rect x="-7" y="-270" width="14" height="14"/><text x="278" transform="rotate(-90)">Garlic</text></g>
    <g class="note out" style="--c:#3a3f42" transform="rotate(170.5)"><rect x="-7" y="-270" width="14" height="14"/><text x="278" transform="rotate(-90)">Sea Salt</text></g>
    <g class="note out" style="--c:#5b7a1e" transform="rotate(174.5)"><rect x="-7" y="-270" width="14" height="14"/><text x="278" transform="rotate(-90)">Kosher Salt</text></g>

    <g class="note in" style="--c:#3a3f42" transform="rotate(183)"><rect x="-7" y="-270" width="14" height="14"/><text x="-278" transform="rotate(90)">Soy Sauce</text></g>
    <g class="note in" style="--c:#4a4a4a" transform="rotate(187)"><rect x="-7" y="-270" width="14" height="14"/><text x="-278" transform="rotate(90)">Fish Sauce</text></g>
    <g class="note in" style="--c:#8a2a1a" transform="rotate(191)"><rect x="-7" y="-270" width="14" height="14"/><text x="-278" transform="rotate(90)">Worcestershire</text></g>
    <g class="note in" style="--c:#d0542a" transform="rotate(195)"><rect x="-7" y="-270" width="14" height="14"/><text x="-278" transform="rotate(90)">Seasoning Sauce</text></g>
    <g class="note in" style="--c:#1aa0b5" transform="rotate(201)"><rect x="-7" y="-270" width="14" height="14"/><text x="-278" transform="rotate(90)">Phosphates</text></g>
    <g class="note in" style="--c:#1a8aa0" transform="rotate(205)"><rect x="-7" y="-270" width="14" height="14"/><text x="-278" transform="rotate(90)">Stocks</text></g>
    <g class="note in" style="--c:#1a4a60" transform="rotate(209)"><rect x="-7" y="-270" width="14" height="14"/><text x="-278" transform="rotate(90)">Lard</text></g>
    <g class="note in" style="--c:#d878b0" transform="rotate(217)"><rect x="-7" y="-270" width="14" height="14"/><text x="-278" transform="rotate(90)">Savourex</text></g>
    <g class="note in" style="--c:#5a4a5a" transform="rotate(221)"><rect x="-7" y="-270" width="14" height="14"/><text x="-278" transform="rotate(90)">MSG</text></g>
    <g class="note in" style="--c:#f26060" transform="rotate(230)"><rect x="-7" y="-270" width="14" height="14"/><text x="-278" transform="rotate(90)">Horseradish</text></g>
    <g class="note in" style="--c:#2a8a3a" transform="rotate(234)"><rect x="-7" y="-270" width="14" height="14"/><text x="-278" transform="rotate(90)">Wasabi</text></g>
    <g class="note in" style="--c:#c8303e" transform="rotate(238)"><rect x="-7" y="-270" width="14" height="14"/><text x="-278" transform="rotate(90)">Pepper</text></g>
    <g class="note in" style="--c:#f08a40" transform="rotate(242)"><rect x="-7" y="-270" width="14" height="14"/><text x="-278" transform="rotate(90)">Cumin</text></g>
    <g class="note in" style="--c:#a02030" transform="rotate(246)"><rect x="-7" y="-270" width="14" height="14"/><text x="-278" transform="rotate(90)">Allspice</text></g>
    <g class="note in" style="--c:#c8203a" transform="rotate(250)"><rect x="-7" y="-270" width="14" height="14"/><text x="-278" transform="rotate(90)">Szechuan</text></g>
    <g class="note in" style="--c:#4a1a5a" transform="rotate(254)"><rect x="-7" y="-270" width="14" height="14"/><text x="-278" transform="rotate(90)">Onion</text></g>
    <g class="note in" style="--c:#6a4a8a" transform="rotate(261.5)"><rect x="-7" y="-270" width="14" height="14"/><text x="-278" transform="rotate(90)">Chipotle</text></g>
    <g class="note in" style="--c:#b01f3f" transform="rotate(265.5)"><rect x="-7" y="-270" width="14" height="14"/><text x="-278" transform="rotate(90)">Jalapeno</text></g>
    <g class="note in" style="--c:#d81a6a" transform="rotate(269.5)"><rect x="-7" y="-270" width="14" height="14"/><text x="-278" transform="rotate(90)">Hot Sauce</text></g>
    <g class="note in" style="--c:#7a1a2a" transform="rotate(273.5)"><rect x="-7" y="-270" width="14" height="14"/><text x="-278" transform="rotate(90)">Habanero</text></g>
    <g class="note in" style="--c:#e0205a" transform="rotate(277.5)"><rect x="-7" y="-270" width="14" height="14"/><text x="-278" transform="rotate(90)">Red Pepper</text></g>
    <g class="note in" style="--c:#f2d000" transform="rotate(281.5)"><rect x="-7" y="-270" width="14" height="14"/><text x="-278" transform="rotate(90)">Mustard</text></g>
    <g class="note in" style="--c:#c8202a" transform="rotate(285.5)"><rect x="-7" y="-270" width="14" height="14"/><text x="-278" transform="rotate(90)">Paprika</text></g>
    <g class="note in" style="--c:#e08a40" transform="rotate(293)"><rect x="-7" y="-270" width="14" height="14"/><text x="-278" transform="rotate(90)">Hard Woods</text></g>
    <g class="note in" style="--c:#b05a10" transform="rotate(297)"><rect x="-7" y="-270" width="14" height="14"/><text x="-278" transform="rotate(90)">Fruit Woods</text></g>
    <g class="note in" style="--c:#1a1a1a" transform="rotate(305)"><rect x="-7" y="-270" width="14" height="14"/><text x="-278" transform="rotate(90)">Charcoal</text></g>
    <g class="note in" style="--c:#2a4a3a" transform="rotate(309)"><rect x="-7" y="-270" width="14" height="14"/><text x="-278" transform="rotate(90)">Whiskey</text></g>
    <g class="note in" style="--c:#5a6a5a" transform="rotate(313)"><rect x="-7" y="-270" width="14" height="14"/><text x="-278" transform="rotate(90)">Bourbon</text></g>
    <g class="note in" style="--c:#c8202a" transform="rotate(321)"><rect x="-7" y="-270" width="14" height="14"/><text x="-278" transform="rotate(90)">Creosote</text></g>
    <g class="note in" style="--c:#b88abf" transform="rotate(333)"><rect x="-7" y="-270" width="14" height="14"/><text x="-278" transform="rotate(90)">Cocktail Bitters</text></g>
    <g class="note in" style="--c:#9a5a9a" transform="rotate(337)"><rect x="-7" y="-270" width="14" height="14"/><text x="-278" transform="rotate(90)">Citric Acid</text></g>
    <g class="note in" style="--c:#8a4a7a" transform="rotate(341)"><rect x="-7" y="-270" width="14" height="14"/><text x="-278" transform="rotate(90)">Tamarind</text></g>
    <g class="note in" style="--c:#0a5a80" transform="rotate(350)"><rect x="-7" y="-270" width="14" height="14"/><text x="-278" transform="rotate(90)">Rice Vinegar</text></g>
    <g class="note in" style="--c:#3a7aa0" transform="rotate(354)"><rect x="-7" y="-270" width="14" height="14"/><text x="-278" transform="rotate(90)">Balsamic Vinegar</text></g>
    <g class="note in" style="--c:#8ab0d0" transform="rotate(358)"><rect x="-7" y="-270" width="14" height="14"/><text x="-278" transform="rotate(90)">Apple Cider Vinegar</text></g>
  </g>

</g>
</svg>
</body>
</html>
```